Compass of Quiet Mornings book cover design

Book cover - the book contains 52 chapters - 2 for each letter of the alphabet, so a yearlong focus on Leadership. The Intent is to communicate that leadership is common sense. It just isn’t common practice. This book allows the reader to focus on one leadership word each week for a yearlong focus on improving one’s leadership. It is full of stories relating to the 52 words that will challenge and inspire the reader.
Target Market(s)
Leaders / Emerging Leaders
Industry/Entity Type
All
Requirements
Must have
- Appeal to executives
Nice to have
- Simplicity
Should not have
- Cartoon feel

```html
<!DOCTYPE html>
<html lang="en">
<head>
<meta charset="utf-8">
<title>Compass of Quiet Mornings — Book Cover</title>
<link rel="stylesheet" href="https://fonts.googleapis.com/css2?family=Anton&display=swap">
<style>
  :root {
    --square-dark: #000000;
    --square-light: #3a3a3c;
    --ink-white: #ffffff;
    --ink-gold: #b08423;
  }
  html, body {
    margin: 0;
    padding: 0;
    width: 849px;
    height: 1200px;
    overflow: hidden;
    background: var(--square-dark);
  }
  .cover {
    display: block;
    width: 849px;
    height: 1200px;
  }
  .board-dark { fill: var(--square-dark); }
  .board-light { fill: var(--square-light); }
  .cover-text {
    font-family: "Anton", "Oswald", sans-serif;
    text-transform: uppercase;
  }
  .author-name { fill: var(--ink-white); }
  .title-main { fill: var(--ink-white); }
  .title-connector { fill: var(--ink-white); }
  .title-accent { fill: var(--ink-gold); }
  .king-piece { fill: var(--ink-gold); }
</style>
</head>
<body>
<svg class="cover" viewBox="0 0 849 1200" xmlns="http://www.w3.org/2000/svg">
  <defs>
    <pattern id="chessboard" x="0" y="0" width="283" height="300" patternUnits="userSpaceOnUse">
      <rect class="board-dark" x="0" y="0" width="141.5" height="150"/>
      <rect class="board-light" x="141.5" y="0" width="141.5" height="150"/>
      <rect class="board-light" x="0" y="150" width="141.5" height="150"/>
      <rect class="board-dark" x="141.5" y="150" width="141.5" height="150"/>
    </pattern>
  </defs>

  <rect class="board" x="0" y="0" width="849" height="1200" fill="url(#chessboard)"/>

  <text class="cover-text author-name" x="253" y="149" font-size="44"
        textLength="319" lengthAdjust="spacingAndGlyphs">Martin Ashford</text>

  <g class="title-block">
    <text class="cover-text title-main" x="68" y="581" font-size="153"
          textLength="620" lengthAdjust="spacingAndGlyphs">Compass</text>

    <rect class="king-piece" role="img" aria-label="Gold chess king piece"
          x="706" y="386" width="54" height="212" rx="6"/>

    <text class="cover-text title-connector" x="72" y="658" font-size="54"
          textLength="159" lengthAdjust="spacingAndGlyphs">Of Quiet</text>

    <text class="cover-text title-accent" x="265" y="749" font-size="168"
          textLength="494" lengthAdjust="spacingAndGlyphs">Mornings</text>
  </g>
</svg>
</body>
</html>
```